Clear Strand Record Protocol Flyer

We need a flyer describing our initiative that seeks to develop and implement a standardized way of describing terrestrial fibre optic networks, which form the backbone of the Internet.
The primary audience that we are targeting is government and development decision makers and regulators, as well as businesses and groups involved in researching, planning, deploying and maintaining fibre optic infrastructure.

```html
<!DOCTYPE html>
<html lang="en">
<head>
<meta charset="utf-8">
<title>Clear Strand Record Protocol Flyer</title>
<link rel="stylesheet" href="https://fonts.googleapis.com/css2?family=Inter:wght@400;600;700&family=Arimo:wght@400;700&family=IBM+Plex+Mono:wght@400;600&display=swap">
<style>
  :root {
    --canvas: #eceeed;
    --ink: #1f1f24;
    --white: #ffffff;
    --violet: #3b2f86;
    --night: #0b0b0d;
    --code-key: #1c2a6b;
    --code-str: #3aa57a;
    --ocean: #1c3f8a;
  }
  * { box-sizing: border-box; margin: 0; padding: 0; }
  html, body { width: 1200px; height: 1200px; overflow: hidden; background: var(--canvas); }
  body { position: relative; font-family: "Arimo", Arial, sans-serif; color: var(--ink); }

  .page { position: absolute; top: 233px; width: 519px; height: 734px; overflow: hidden; }
  .page-front { left: 54px; background: var(--night); }
  .page-back { left: 627px; }

  .hero-photo {
    position: absolute; inset: 0 0 220px 0;
    background:
      radial-gradient(ellipse at 48% 40%, #8d8f94 0%, #55585e 30%, transparent 62%),
      linear-gradient(180deg, #2a2b2f 0%, #4b4d52 40%, #1a1b1e 78%, var(--night) 100%);
  }
  .hero-fade { position: absolute; left: 0; right: 0; top: 380px; height: 150px;
    background: linear-gradient(180deg, transparent, var(--night)); }

  .brand { position: absolute; left: 37px; top: 26px; color: var(--white);
    font-family: "Inter", Arial, sans-serif;
    font-size: 56px; font-weight: 400; letter-spacing: -2px; line-height: 1; }

  .tagline { position: absolute; left: 0; right: 0; top: 416px; text-align: center;
    font-family: "IBM Plex Mono", "Courier New", monospace; color: var(--white);
    font-size: 12.4px; line-height: 14.5px; }
  .intro { position: absolute; left: 48px; right: 48px; top: 471px; text-align: center;
    color: var(--white); font-size: 10.6px; line-height: 12.6px; }

  .panel { position: absolute; left: 37px; width: 445px; background: var(--white); }
  .panel-title { position: absolute; left: 37px; width: 223px; height: 37px;
    font-family: "Inter", Arial, sans-serif;
    background: var(--violet); color: var(--white); font-weight: 700; font-size: 12.6px;
    padding: 0 18px; line-height: 37px; z-index: 2; }
  .panel-body { padding: 30px 17px 8px 18px; font-size: 8.7px; line-height: 10.5px; }
  .panel-body p + p { margin-top: 10.5px; }

  .footer { position: absolute; left: 37px; top: 683px; display: flex; align-items: center;
    gap: 6px; color: var(--white); font-size: 11px; }
  .footer .dot { width: 17px; height: 17px; background: var(--violet); border-radius: 3px; display: flex; align-items: center; justify-content: center; }
  .footer .social { margin-left: 10px; font-weight: 700; font-size: 13px; }

  .ocean-photo { position: absolute; inset: 0;
    background:
      radial-gradient(ellipse at 80% 20%, #2f64c4 0%, transparent 50%),
      radial-gradient(ellipse at 20% 85%, #3a72cf 0%, transparent 45%),
      linear-gradient(160deg, #143476 0%, var(--ocean) 45%, #10306c 100%); }

  .data-row { position: relative; display: flex; gap: 8px; margin-top: 6px; height: 193px; }
  .code { width: 200px; padding-left: 10px; font-family: "IBM Plex Mono", monospace;
    font-size: 5.4px; line-height: 7.35px; white-space: pre; color: var(--code-key); }
  .code .k { font-weight: 600; }
  .code .s { color: var(--code-str); }
  .map { position: absolute; left: 212px; top: 0; width: 192px; height: 193px;
    background: linear-gradient(135deg, #bcd6a8 0%, #d9e6c8 45%, #c9ddb5 100%); }
  .caption { text-align: center; margin-top: 11px; }
  .benefits { list-style: none; }
  .benefits li { position: relative; padding-left: 10px; }
  .benefits li::before { content: ""; position: absolute; left: 1px; top: 3.5px; width: 4px; height: 4px; border-radius: 50%; background: var(--ink); }
  .benefits b { font-weight: 700; }
</style>
</head>
<body>

<section class="page page-front">
  <div class="hero-photo" role="img" aria-label="Photo of a technician working at a laptop in a server room"></div>
  <div class="hero-fade"></div>
  <div class="brand">csrp</div>
  <p class="tagline">Everyone deserves access to affordable<br>and reliable Internet, no matter their location<br>or circumstance.</p>
  <p class="intro">Meeting this challenge requires a community working together, ideally using shared standards and data to ensure the networks they plan and build interconnect with the global Internet.</p>

  <h2 class="panel-title" style="top:527px;">What's the Problem?</h2>
  <div class="panel" style="top:545px;min-height:128px;">
    <div class="panel-body">
      <p>Fibre optic infrastructure forms the backbone of the Internet, underpinning all Internet access technologies, including mobile, wireless, and satellite.</p>
      <p>Despite its importance, the telecom sector and relevant government agencies often lack consistent and readily available data to help them plan, maintain, expand, and protect it.</p>
      <p>This can cause multiple problems, including unknowingly duplicating existing infrastructure, not identifying gaps or single points of failure in current infrastructure, and not being able to effectively measure the socioeconomic impact of investments in Internet infrastructure.</p>
    </div>
  </div>

  <div class="footer">
    <span class="dot"><svg width="11" height="11" viewBox="0 0 12 12" fill="none" stroke="#fff" stroke-width="1"><circle cx="6" cy="6" r="5"/><ellipse cx="6" cy="6" rx="2.2" ry="5"/><line x1="1" y1="6" x2="11" y2="6"/></svg></span>
    <span>clearstrand.info</span>
    <span class="social">Netlink</span>
  </div>
</section>

<section class="page page-back">
  <div class="ocean-photo" role="img" aria-label="Blue abstract photo of glowing fibre optic strands"></div>

  <h2 class="panel-title" style="top:33px;">How does CSRP Solve This?</h2>
  <div class="panel" style="top:52px;min-height:357px;">
    <div class="panel-body" style="padding-top:27px;">
      <p>The Clear Strand Record Protocol (CSRP) is a common language for describing terrestrial fibre optic networks. It also works to establish norms among operators and regulators for information sharing regarding terrestrial fibre deployments.</p>
      <p>The standard facilitates the exchange, analysis, and visualization of fibre network data for different stakeholders, including governments, telecom providers, and researchers.</p>
      <p>By providing a consistent schema, CSRP enhances interoperability, transparency, and informed decision-making in broadband expansion and resilience efforts.</p>
      <div class="data-row">
<div class="code">{
  <span class="k">"networks"</span>: [
    {
      <span class="k">"id"</span>: <span class="s">"febb76d1-ddd6-466f-ada6-9419572b830b"</span>,
      <span class="k">"name"</span>: <span class="s">"Brazil"</span>,
      <span class="k">"nodes"</span>: [
        {
          <span class="k">"id"</span>: <span class="s">"0"</span>,
          <span class="k">"name"</span>: <span class="s">"Calcoene"</span>,
          <span class="k">"region"</span>: <span class="s">"AMS"</span>,
          <span class="k">"location"</span>: {
            <span class="k">"type"</span>: <span class="s">"Point"</span>,
            <span class="k">"coordinates"</span>: [
              -50.945839,
              2.496629
            ]
          },
          <span class="k">"address"</span>: {
            <span class="k">"country"</span>: <span class="s">"BR"</span>
          },
          <span class="k">"status"</span>: <span class="s">"operational"</span>
        },
        {
          <span class="k">"id"</span>: <span class="s">"1"</span>,
          <span class="k">"name"</span>: <span class="s">"Amapa"</span>,
          <span class="k">"region"</span>: <span class="s">"AMS"</span>,
          <span class="k">"location"</span>: {</div>
        <div class="map" role="img" aria-label="Map visualization of a national fibre network with coloured spans and nodes by status"></div>
      </div>
      <p class="caption">On the left, a snapshot of CSRP data describing Brazil's fibre network.<br>On the right, visualization of CSRP data.</p>
    </div>
  </div>

  <h2 class="panel-title" style="top:418px;">Who Benefits?</h2>
  <div class="panel" style="top:436px;min-height:118px;">
    <div class="panel-body" style="padding-top:27px;">
      <ul class="benefits">
        <li><b>Governments and communication regulators</b> can assess national network infrastructure holistically to identify gaps in infrastructure and areas of network fragility. CSRP also helps avoid duplication in reporting of fibre infrastructure where multiple operators may report fibre on a single deployment.</li>
        <li><b>Investors and planners</b> can make more informed data-driven decisions on infrastructure development.</li>
        <li><b>Surveyors, engineers, and researchers</b> can access standardized data through GIS tools and mapping platforms.</li>
      </ul>
    </div>
  </div>

  <h2 class="panel-title" style="top:564px;">Who's Involved?</h2>
  <div class="panel" style="top:582px;min-height:117px;">
    <div class="panel-body" style="padding-top:27px;">
      <p>Established in 2022, the CSRP has been developed in collaboration with the Global Development Fund, International Signal Union, the Open Net Society, Firelight Corporation, Tidewater Connect, CubeLink, and Digital Forum Africa.</p>
      <p>The Open Net Society assumed a secretariat role for the standard in 2025 and is working to advance awareness and adoption of it worldwide through in-person workshops and technical assistance.</p>
      <p>Join our community to inform policy and investment decisions that can make the Internet for everyone.</p>
    </div>
  </div>
</section>

</body>
</html>
```